Summer Music/Chorus/Choir Camp for Young Singers Ages 8-13

We need a flyer for a summer camp for young singers ages 8-13. We are nonprofit community children's chorus in Miami, FL. Our camp provides specialized training in music theory, sight-reading,and aural training through daily choral rehearsals in an environment that is both positive and a lot of fun! Our camp offers children the opportunity to come as they are, no matter the level of experience, and grow tremendously in their musicianship skills. In addition to this, our campers participate in song-writing, masterclasses, community performances, and media projects. The final design should be clean, fun, not too crowded, should appeal to boys and girls ages 8-13, and something someone that age would consider "cool" and not too childish. Drawings are cool, something different.
Updates

Target Market(s)

Ages 8-13 and parents of those kids.

Industry/Entity Type

Community

Requirements
Must have
• All info attached.
Nice to have
• Things that relate to music, especially related to singing/choirs
Should not have
• instruments, stock photos of children, or photos from our website (unless they are used very creatively), or photos in general. I've attached our previous camp flyer and our current organization flyer but I don't necessarily want this flyer to look like those.

```html
<!DOCTYPE html>
<html lang="en">
<head>
<meta charset="utf-8">
<title>Choral Camp Flyer</title>
<link rel="stylesheet" href="https://fonts.googleapis.com/css2?family=Montserrat:wght@600;700;800&family=Bebas+Neue&family=Oswald:wght@700&family=Courier+Prime:wght@700&display=swap">
<style>
  :root{
    --aqua-light:#d6f1ee;
    --aqua:#bfe6e2;
    --aqua-mid:#9fd6d1;
    --teal:#2f6f6b;
    --teal-dark:#1f5552;
    --teal-band:#3b7f79;
    --pale-text:#cdeeea;
    --gold:#f2dc8c;
    --cream:#f7e8a4;
    --red:#e0342a;
    --white:#ffffff;
  }
  html,body{margin:0;padding:0;overflow:hidden;}
  body{width:805px;height:1200px;background:var(--aqua-light);}
  .flyer{position:relative;width:805px;height:1200px;overflow:hidden;
    background:linear-gradient(180deg,var(--aqua) 0%,var(--aqua-light) 45%,var(--aqua) 100%);
    font-family:"Montserrat",Arial,sans-serif;}
  .abs{position:absolute;}
  .choir-photo{left:0;top:0;width:805px;height:380px;
    background:linear-gradient(180deg,#7fbeb8 0%,#a9dad5 55%,rgba(191,230,226,0) 100%);}
  .notes-area{left:0;top:660px;width:805px;height:420px;
    background:radial-gradient(ellipse 220px 170px at 22% 45%,rgba(255,255,255,.65),rgba(255,255,255,0) 100%),
               radial-gradient(ellipse 200px 180px at 86% 55%,rgba(255,255,255,.55),rgba(255,255,255,0) 100%),
               radial-gradient(ellipse 260px 90px at 50% 20%,rgba(255,255,255,.45),rgba(255,255,255,0) 100%);}
  .staff-curves{left:0;top:0;width:805px;height:1200px;}
  .brand{left:230px;top:66px;width:345px;text-align:center;color:var(--teal);font-weight:700;}
  .brand .small{font-size:16px;display:block;line-height:20px;}
  .brand .big{font-size:34px;line-height:44px;display:block;white-space:nowrap;}
  .title-music{left:270px;top:323px;width:263px;height:85px;border:3px solid var(--pale-text);
    box-sizing:border-box;display:flex;align-items:center;justify-content:center;
    font-size:60px;font-weight:800;color:var(--gold);letter-spacing:2px;}
  .title-sub{left:200px;top:420px;width:408px;text-align:center;color:var(--pale-text);
    font-size:44px;font-weight:700;line-height:48px;}
  .rule{height:2px;background:var(--pale-text);}
  .dates{left:200px;top:544px;width:408px;text-align:center;font-family:"Courier Prime",monospace;font-weight:700;}
  .dates .d1{color:var(--gold);font-size:36px;display:block;line-height:40px;}
  .dates .d2{color:var(--white);font-size:27px;display:block;line-height:34px;}
  .price{left:20px;top:500px;width:170px;height:211px;background:var(--teal-band);box-sizing:border-box;padding:8px;}
  .price-inner{background:var(--cream);height:100%;text-align:center;box-sizing:border-box;padding-top:10px;}
  .price .amount{color:var(--red);font-family:"Oswald",sans-serif;font-size:58px;font-weight:700;line-height:70px;display:block;}
  .price .session{color:var(--teal);font-size:19px;font-weight:800;line-height:21px;display:block;margin-top:4px;}
  .price .note{color:var(--teal-dark);font-family:"Bebas Neue",sans-serif;font-size:15px;line-height:16px;display:block;margin-top:12px;}
  .invite{left:575px;top:251px;width:184px;height:184px;border-radius:50%;background:var(--cream);
    text-align:center;display:flex;flex-direction:column;justify-content:center;box-shadow:0 0 0 2px var(--aqua-light),0 0 0 3px var(--teal);}
  .invite .lead{font-family:"Bebas Neue",sans-serif;color:var(--teal);font-size:21px;line-height:22px;}
  .invite .cta{color:var(--red);font-weight:800;font-size:23px;line-height:25px;margin-top:4px;}
  .extended{left:567px;top:555px;width:216px;height:216px;border-radius:50%;background:var(--red);
    color:var(--white);font-family:"Bebas Neue",sans-serif;font-size:26px;line-height:27px;text-align:center;
    display:flex;align-items:center;justify-content:center;box-shadow:0 0 0 6px var(--aqua-light),0 0 0 7px var(--teal);}
  .venue{left:130px;top:752px;width:545px;text-align:center;color:var(--red);font-weight:700;font-size:20px;line-height:25px;}
  .dotline{border-top:3px dotted var(--teal-dark);}
  .call{left:150px;top:858px;width:505px;text-align:center;color:var(--teal-dark);font-family:"Bebas Neue",sans-serif;font-size:36px;}
  .phone{left:150px;top:898px;width:505px;text-align:center;color:var(--teal-dark);font-weight:800;font-size:56px;letter-spacing:-1px;}
  .email{left:150px;top:968px;width:505px;text-align:center;color:var(--teal-dark);font-weight:700;font-size:21px;
    border-top:2px dashed var(--teal-dark);border-bottom:2px dashed var(--teal-dark);padding:3px 0;}
  .clouds{left:0;top:1020px;width:805px;height:180px;}
  .sponsor{color:var(--teal-dark);font-weight:700;font-size:15px;}
  .badge{left:387px;top:1031px;width:62px;height:62px;background:var(--teal-dark);}
  .footer-band{left:178px;top:1120px;width:431px;height:80px;background:var(--teal-band);color:var(--white);
    font-family:"Bebas Neue",sans-serif;font-size:16px;line-height:19px;text-align:center;box-sizing:border-box;
    padding-top:18px;}
  .footer-band::before,.footer-band::after{content:"";position:absolute;left:8px;right:8px;border-top:2px dotted var(--white);}
  .footer-band::before{top:8px;}
  .footer-band::after{bottom:12px;}
</style>
</head>
<body>
<div class="flyer">
  <div class="abs choir-photo" role="img" aria-label="Photo of a young conductor leading a children's choir on stage"></div>
  <div class="abs notes-area" role="img" aria-label="Scattered white music notes and clefs floating across the lower background"></div>

  <svg class="abs staff-curves" viewBox="0 0 805 1200" aria-hidden="true">
    <g fill="none" stroke="#ffffff" stroke-width="1.5" stroke-dasharray="6 6" opacity=".7">
      <path d="M0 560 C120 520 160 640 60 760"/>
      <path d="M40 820 C140 760 220 860 180 980"/>
      <path d="M805 820 C700 780 640 880 700 1000"/>
      <path d="M720 180 C790 230 800 320 760 400"/>
    </g>
  </svg>

  <svg class="abs clouds" viewBox="0 0 805 180" aria-hidden="true">
    <ellipse cx="120" cy="160" rx="200" ry="80" fill="#cfeeea"/>
    <ellipse cx="420" cy="175" rx="260" ry="75" fill="#d7f2ef"/>
    <ellipse cx="720" cy="150" rx="180" ry="85" fill="#cfeeea"/>
  </svg>

  <div class="abs brand"><span class="small">The</span><span class="big">Young Harmony</span><span class="small">Chorus</span></div>

  <svg class="abs" style="left:0;top:0" width="805" height="800" aria-hidden="true">
    <circle cx="404" cy="464" r="242" fill="none" stroke="#2f6f6b" stroke-width="1.5"/>
    <circle cx="404" cy="464" r="232" fill="#2f6f6b"/>
    <circle cx="404" cy="464" r="226" fill="none" stroke="#f2dc8c" stroke-width="2"/>
  </svg>

  <div class="abs title-music">MUSIC</div>
  <div class="abs title-sub">BLAST AT OUR<br>CHORAL CAMP</div>
  <div class="abs rule" style="left:232px;top:536px;width:345px"></div>
  <div class="abs dates"><span class="d1">JULY 18-29</span><span class="d2">9AM-3PM (M-F)</span></div>
  <div class="abs rule" style="left:284px;top:624px;width:240px"></div>

  <div class="abs price"><div class="price-inner">
    <span class="amount">$300</span>
    <span class="session">FOR 2-WEEK<br>SESSION</span>
    <span class="note">PRICE DOES NOT INCLUDE<br>LUNCH</span>
  </div></div>

  <div class="abs invite">
    <div class="lead">SINGERS IN<br>GRADES 3-9 ARE<br>INVITED TO ATTEND</div>
    <div class="cta">REGISTER<br>TODAY!</div>
  </div>

  <div class="abs extended">EXTENDED<br>HOURS AVAILABLE<br>(7:30AM-5:30PM)<br>FOR AN EXTRA $50<br>PER WEEK.</div>

  <div class="abs venue">SOUTHBAY<br>CULTURAL ARTS CENTER, 4820 SW<br>118TH STREET MIAMI, FL 33176</div>
  <div class="abs dotline" style="left:177px;top:840px;width:431px"></div>

  <div class="abs call">CALL US TO REGISTER TODAY</div>
  <div class="abs phone">305.555.0148</div>
  <div class="abs email">INFO@YOUNGHARMONYCHORUS.ORG</div>

  <div class="abs sponsor" style="left:174px;top:1052px">Larkfield Foundation</div>
  <div class="abs badge" role="img" aria-label="Partner badge"></div>
  <div class="abs sponsor" style="left:485px;top:1052px">Coral Shore County</div>

  <div class="abs footer-band">THE YOUNG HARMONY CHORUS IS A 501 (C)(3) NONPROFIT ORGANIZATION.<br>DONATIONS MADE TO YHC ARE TAX-EXEMPT</div>
</div>
</body>
</html>
```